CD Cover Design Project

Although I posted a picture as a possible idea, an idea from scratch is mostly what I am looking for. Definitely listen to the song before making the design. The link is posted right here in the project overview.
I need a CD cover for my latest single. This artwork will go up on Melodeck, brimora, etc with the song. Please listen to the song and then creat the artwork. Here is a link to the song:
http://tunevaultmusic.net/doriancolewhitfield/where-the-rivers-bend
The design needs my name, Dorian Cole Whitfield and it needs the song title, Where the Rivers Bend.
It needs to be a perfect square.
1600 by 1600
Resolution 300 DPI
Contact me at dorian@dorian-cole.net or (503) 482-3091

```html
<!DOCTYPE html>
<html lang="en">
<head>
<meta charset="utf-8">
<title>Where the Rivers Bend — Dorian Cole Whitfield</title>
<link href="https://fonts.googleapis.com/css2?family=Abril+Fatface&family=Bebas+Neue&family=Oswald:wght@500;700&family=Playfair+Display:wght@700;900&family=Special+Elite&family=UnifrakturMaguntia&family=Mrs+Saint+Delafield&display=swap" rel="stylesheet">
<style>
  :root {
    --stage-glow: #e9dcc0;
    --stage-mid: #8a7656;
    --stage-dark: #15110c;
    --ink: #141210;
    --paper: #ece3d0;
    --paper-warm: #d9ccb1;
    --signature: #cdb48a;
  }
  html, body {
    margin: 0;
    padding: 0;
    width: 1200px;
    height: 1200px;
    overflow: hidden;
    background: var(--stage-dark);
  }
  .cover {
    position: relative;
    width: 1200px;
    height: 1200px;
    overflow: hidden;
  }
  .stage-photo {
    position: absolute;
    inset: 0;
    background:
      radial-gradient(ellipse 55% 40% at 50% 22%, rgba(233,220,192,0.85), rgba(233,220,192,0) 70%),
      radial-gradient(ellipse 35% 30% at 47% 60%, rgba(200,180,140,0.55), rgba(200,180,140,0) 75%),
      linear-gradient(180deg, #5e513d 0%, #3a3024 45%, #1c1711 75%, var(--stage-dark) 100%);
  }
  .stage-photo::after {
    content: "";
    position: absolute;
    inset: 0;
    background: radial-gradient(ellipse 80% 80% at 50% 45%, rgba(0,0,0,0) 45%, rgba(0,0,0,0.75) 100%);
  }
  .title {
    position: absolute;
    inset: 0;
    margin: 0;
    font-weight: normal;
  }
  .word {
    position: absolute;
    display: flex;
    align-items: flex-end;
    gap: 4px;
  }
  .word--where  { left: 235px; top: 270px; }
  .word--the    { left: 640px; top: 225px; }
  .word--rivers { left: 120px; top: 485px; }
  .word--bend   { left: 690px; top: 405px; }
  .tile {
    display: inline-block;
    line-height: 1;
    color: var(--ink);
    padding: 6px 8px 8px;
    font-size: 104px;
  }
  .tile--paper { background: var(--paper); }
  .tile--warm  { background: var(--paper-warm); }
  .tile--ink   { background: var(--ink); color: var(--paper); }
  .tile--bare  { background: transparent; padding: 6px 2px; }
  .face-a { font-family: "Playfair Display", serif; font-weight: 900; }
  .face-b { font-family: "Bebas Neue", sans-serif; font-size: 118px; }
  .face-c { font-family: "Special Elite", monospace; }
  .face-d { font-family: "Abril Fatface", serif; }
  .face-e { font-family: "Oswald", sans-serif; font-weight: 700; }
  .face-f { font-family: "UnifrakturMaguntia", serif; }
  .tilt-l  { transform: rotate(-4deg); }
  .tilt-r  { transform: rotate(3deg); }
  .drop    { transform: translateY(10px); }
  .lift    { transform: translateY(-8px) rotate(-2deg); }
  .artist {
    position: absolute;
    left: 0;
    right: 0;
    bottom: 18px;
    margin: 0;
    text-align: center;
    font-family: "Mrs Saint Delafield", cursive;
    font-weight: normal;
    font-size: 74px;
    letter-spacing: 2px;
    color: var(--signature);
  }
</style>
</head>
<body>
  <main class="cover">
    <div class="stage-photo" role="img" aria-label="Sepia concert photograph: a singer in shirt and tie playing acoustic guitar at a microphone, lit by stage spotlights, with amplifiers and drums behind and audience silhouettes in front"></div>

    <h1 class="title" aria-label="Where the Rivers Bend">
      <span class="word word--where" aria-hidden="true">
        <span class="tile tile--paper face-a tilt-l">W</span>
        <span class="tile tile--bare face-c drop">h</span>
        <span class="tile tile--warm face-e lift">e</span>
        <span class="tile tile--paper face-d tilt-r">r</span>
        <span class="tile tile--bare face-c drop">e</span>
      </span>
      <span class="word word--the" aria-hidden="true">
        <span class="tile tile--ink face-b tilt-r">t</span>
        <span class="tile tile--paper face-a lift">h</span>
        <span class="tile tile--bare face-f drop">e</span>
      </span>
      <span class="word word--rivers" aria-hidden="true">
        <span class="tile tile--bare face-f tilt-l">R</span>
        <span class="tile tile--paper face-e drop">i</span>
        <span class="tile tile--warm face-a lift">v</span>
        <span class="tile tile--bare face-c tilt-r">e</span>
        <span class="tile tile--paper face-d drop">r</span>
        <span class="tile tile--bare face-c lift">s</span>
      </span>
      <span class="word word--bend" aria-hidden="true">
        <span class="tile tile--paper face-a tilt-r">B</span>
        <span class="tile tile--bare face-c drop">e</span>
        <span class="tile tile--ink face-b lift">n</span>
        <span class="tile tile--warm face-d tilt-l">d</span>
      </span>
    </h1>

    <p class="artist">Dorian Cole Whitfield</p>
  </main>
</body>
</html>
```